New Business Card Design Project

We want a modern business card that catches the attention of other remodeling companies as well as homeowners. We would like it to be informative but still simple.

Target Market(s)

Residential and other Business's

Contact Information for Business Card

TrellBrix
Phone number is 5153927048
Address is
4817 SW 3rd Lane
Des Moines, Iowa 50313
email is trellbrixco@quamlet.com

Requirements
Must have
• Our tagline
• Honest | Professional | Affordable

```html
<!DOCTYPE html>
<html lang="en">
<head>
<meta charset="utf-8">
<title>TrellBrix Business Card</title>
<link rel="stylesheet" href="https://fonts.googleapis.com/css2?family=Oswald:wght@500&family=Poppins:wght@500;700&display=swap">
<style>
  :root {
    --charcoal: #434142;
    --brand-blue: #3a5fb8;
    --brand-orange: #e0501d;
    --ink: #333132;
    --paper: #ffffff;
    --backdrop: #ffffff;
    --shadow: rgba(0,0,0,0.35);
  }
  * { margin: 0; padding: 0; box-sizing: border-box; }
  html, body {
    width: 1200px; height: 1200px; overflow: hidden;
    background: var(--backdrop);
    font-family: "Poppins", sans-serif;
  }
  .canvas { position: relative; width: 1200px; height: 1200px; }

  .card {
    position: absolute; left: 220px; width: 760px; height: 456px;
    box-shadow: 6px 6px 6px var(--shadow);
  }
  .card-front {
    top: 106px;
    background: var(--charcoal);
    border-left: 8px solid var(--brand-blue);
    border-bottom: 8px solid var(--brand-blue);
  }
  .card-back {
    top: 636px;
    background: var(--paper);
    border: 1px solid #d8d8d8;
  }

  .wordmark {
    position: absolute; left: 0; right: 0; text-align: center;
    font-family: "Poppins", sans-serif; font-weight: 700;
    letter-spacing: 2px; line-height: 1; white-space: nowrap;
  }
  .card-front .wordmark {
    top: 172px; font-size: 98px; color: var(--paper); padding-right: 8px;
  }
  .tagline {
    position: absolute; left: 0; right: 0; text-align: center;
    font-family: "Oswald", sans-serif; font-weight: 500;
    text-transform: uppercase; white-space: nowrap; line-height: 1;
  }
  .card-front .tagline {
    top: 272px; font-size: 30px; letter-spacing: 0.5px; color: var(--paper); padding-right: 8px;
  }
  .tagline .sep { display: inline-block; margin: 0 8px; color: var(--brand-blue); }

  .back-brand { position: absolute; left: 58px; top: 170px; width: 340px; }
  .card-back .wordmark {
    position: static; font-size: 54px; color: var(--brand-blue); letter-spacing: 1px;
  }
  .card-back .tagline {
    position: static; margin-top: 10px; font-size: 17px; letter-spacing: 0.5px;
    color: var(--brand-blue);
  }
  .card-back .tagline .sep { margin: 0 4px; color: var(--brand-orange); }

  .divider {
    position: absolute; left: 401px; top: 110px; width: 2px; height: 178px;
    background: var(--ink);
  }

  .contact-list { position: absolute; left: 428px; top: 178px; list-style: none; }
  .contact-item {
    position: relative; padding-left: 37px;
    font-size: 18px; font-weight: 500; color: var(--ink); line-height: 26px;
    white-space: nowrap;
  }
  .contact-item + .contact-item { margin-top: 5px; }
  .contact-item.address { margin-top: 12px; }
  .contact-item svg { position: absolute; left: 0; top: 3px; width: 20px; height: 20px; fill: var(--brand-blue); }

  .services-title {
    position: absolute; left: 0; right: 0; top: 316px; text-align: center;
    font-size: 33px; font-weight: 500; color: var(--brand-blue);
  }
  .services-list {
    position: absolute; left: 0; right: 0; top: 368px; text-align: center;
    font-size: 28px; font-weight: 500; color: var(--ink); white-space: nowrap;
    list-style: none;
  }
  .services-list li { display: inline; }
  .services-list li::before { content: "•"; color: var(--brand-blue); margin: 0 10px 0 8px; }
</style>
</head>
<body>
<main class="canvas">
  <section class="card card-front" aria-label="Card front">
    <div class="wordmark">TRELLBRIX</div>
    <div class="tagline">Honest<span class="sep">|</span>Professional<span class="sep">|</span>Affordable</div>
  </section>

  <section class="card card-back" aria-label="Card back">
    <div class="back-brand">
      <div class="wordmark">TRELLBRIX</div>
      <div class="tagline">Honest<span class="sep">|</span>Professional<span class="sep">|</span>Affordable</div>
    </div>

    <div class="divider"></div>

    <ul class="contact-list">
      <li class="contact-item">
        <svg viewBox="0 0 24 24" aria-hidden="true"><path d="M6.6 10.8a15.1 15.1 0 0 0 6.6 6.6l2.2-2.2a1 1 0 0 1 1-.25 11.4 11.4 0 0 0 3.6.57 1 1 0 0 1 1 1V20a1 1 0 0 1-1 1A17 17 0 0 1 3 4a1 1 0 0 1 1-1h3.5a1 1 0 0 1 1 1c0 1.25.2 2.45.57 3.57a1 1 0 0 1-.25 1z"/></svg>
        515 392 7048
      </li>
      <li class="contact-item">
        <svg viewBox="0 0 24 24" aria-hidden="true"><path d="M2 5h20v14H2z M4 7v.3l8 5.4 8-5.4V7z M4 9.7V17h16V9.7l-8 5.4z" fill-rule="evenodd"/></svg>
        trellbrixco@quamlet.com
      </li>
      <li class="contact-item address">
        <svg viewBox="0 0 24 24" aria-hidden="true"><path d="M12 2a7 7 0 0 0-7 7c0 5.2 7 13 7 13s7-7.8 7-13a7 7 0 0 0-7-7zm0 9.5A2.5 2.5 0 1 1 12 6.5a2.5 2.5 0 0 1 0 5z"/></svg>
        4817 SW 3rd Lane<br>Des Moines, Iowa 50313
      </li>
    </ul>

    <h2 class="services-title">Install and Repair</h2>
    <ul class="services-list">
      <li>Faucet</li><li>Shower</li><li>Pipe</li><li>Water heater</li><li>Toilet</li>
    </ul>
  </section>
</main>
</body>
</html>
```